Corvanti, LLC Website

Creating website for medical billing company.

Target Market(s)

Medical providers

Industry/Entity Type

Medical billing

Coding

Coded - Design and coding required

Number of Pages Required

3 page

Font styles to use
Other font styles liked:
• Fonts that match our logo.

Requirements
Must have
• First page (greeting and explanation of who we are). Second page something about me and company (I'll supply some content, make generic for now). And page three, information that people can give for us to contact them.
Nice to have
• A little animation. But not over-the-top. Colors that match our logo.
Should not have
• Over-the-top animation.

```html
<!DOCTYPE html>
<html lang="en">
<head>
<meta charset="utf-8">
<title>Corvanti, LLC — Medical Billing</title>
<link href="https://fonts.googleapis.com/css2?family=Noto+Sans:wght@400;600;700&family=Open+Sans:wght@300;400;600;700&display=swap" rel="stylesheet">
<style>
:root{
  --navy:#1f3552;
  --navy-deep:#18304b;
  --royal:#2b4472;
  --teal:#00a9d6;
  --teal-bright:#0fb3e0;
  --blue-btn:#3d9be0;
  --ink:#1f2f4d;
  --grey-text:#777;
  --topbar:#4a4a4a;
  --light:#f4f4f4;
  --field:#eef3fa;
}
*{box-sizing:border-box;margin:0;padding:0}
html,body{width:1200px;height:3683px;overflow:hidden}
body{position:relative;font-family:"Open Sans",sans-serif;color:var(--ink);background:#fff}
.abs{position:absolute}
.heading{font-family:"Noto Sans",sans-serif}

.topbar{left:0;top:0;width:1200px;height:30px;background:var(--topbar);color:#fff;font-size:12px}
.topbar span{position:absolute;top:8px;display:flex;align-items:center;gap:6px}
.topbar b{font-weight:700}

.nav{left:0;top:30px;width:1200px;height:79px;background:#fff}
.brand{position:absolute;display:flex;align-items:center;gap:8px;font-family:"Open Sans",sans-serif;font-weight:600;color:var(--navy)}
.brand i{display:block;border-radius:50%;background:var(--teal)}
.nav .brand{left:128px;top:26px;font-size:17px}
.nav .brand i{width:22px;height:22px}
.nav a{position:absolute;top:33px;font-size:15px;font-weight:600;color:#555;text-decoration:none;letter-spacing:.3px}
.nav a.active{color:var(--royal);font-weight:700}

.hero{left:0;top:109px;width:1200px;height:673px;background:linear-gradient(100deg,#1b2a3a 0%,#2c3c4c 45%,#4b5660 70%,#2a3540 100%)}
.hero .shade{position:absolute;inset:0;background:linear-gradient(90deg,rgba(15,25,40,.55),rgba(15,25,40,.1))}
.hero-label{left:96px;top:325px;font-size:13px;color:#fff;display:flex;align-items:center;gap:12px}
.hero-label:after{content:"";width:46px;height:1px;background:#fff}
.hero-title{left:96px;top:370px;font-size:44px;line-height:58px;font-weight:700;color:#fff;letter-spacing:.5px;white-space:nowrap}
.hero-text{left:96px;top:504px;width:580px;font-size:13px;line-height:21px;color:#fff}
.btn-discover{left:96px;top:598px;width:191px;height:40px;background:var(--blue-btn);color:#fff;font-size:12px;font-weight:700;display:flex;align-items:center;justify-content:center}

.eyebrow{font-size:11px;font-weight:700;color:#555;letter-spacing:.4px}
.rule{height:3px;background:var(--teal)}
.about-img{left:74px;top:873px}
.about .eyebrow{left:613px;top:891px}
.about h2{left:613px;top:918px;font-size:37px;font-weight:400;color:var(--ink)}
.about .rule{left:613px;top:979px;width:86px}
.about h3{left:613px;top:1010px;font-size:21px;font-weight:400;color:var(--teal)}
.about p{left:613px;top:1062px;width:490px;font-size:14.5px;line-height:24px;color:var(--grey-text);font-weight:300}
.feature{top:1218px;display:flex;align-items:center;gap:14px;font-family:"Noto Sans",sans-serif;font-weight:700;font-size:16px;line-height:24px;color:var(--ink)}
.btn-contact{left:613px;top:1314px;width:155px;height:45px;background:var(--teal-bright);color:#fff;font-weight:700;font-size:16px;display:flex;align-items:center;justify-content:center;gap:14px}

.services{left:0;top:1477px;width:1200px;height:615px;background:var(--light)}
.center{left:0;width:1200px;text-align:center}
.card-img{top:1746px;width:321px;height:216px}
.card-tag{top:1933px;height:56px;width:269px;background:#fff;box-shadow:0 4px 14px rgba(0,0,0,.08);display:flex;align-items:center;font-size:14.5px;color:var(--ink)}
.card-tag .ico{width:56px;height:56px;background:var(--teal-bright);display:flex;align-items:center;justify-content:center;margin-right:30px}

.why{left:0;top:2092px;width:1200px;height:549px;background:linear-gradient(110deg,#2d4775 0%,#2a4270 40%,#34507f 65%,#2a416c 100%)}
.why-col{top:2335px;width:330px;text-align:center;color:#fff}
.why-col .circ{width:74px;height:74px;border-radius:50%;background:#fff;margin:0 auto;display:flex;align-items:center;justify-content:center}
.why-col h4{font-family:"Noto Sans",sans-serif;font-size:19px;font-weight:700;margin-top:33px}
.why-col p{font-size:14.5px;line-height:24px;margin-top:18px;font-weight:300}
.why-col .appt{font-size:11.5px;font-weight:700;margin-top:12px;display:flex;justify-content:center;align-items:center;gap:8px;letter-spacing:.3px}

.wave{left:0;top:3100px}
.card{left:164px;top:2942px;width:874px;height:456px;background:#fff;box-shadow:0 6px 24px rgba(0,0,0,.08)}
.card .topline{position:absolute;left:38px;top:0;width:795px;height:4px;background:#4b5d73}
.card h3{position:absolute;left:51px;top:55px;font-size:29px;line-height:36px;font-weight:400;color:var(--ink)}
.field{position:absolute;left:51px;width:344px;background:var(--field);border-radius:3px;font-size:11.5px;color:#888;padding:14px 15px}
.submit{position:absolute;left:51px;top:334px;width:188px;height:49px;background:var(--navy);color:#fff;font-weight:700;font-size:16px;display:flex;align-items:center;justify-content:center}
.card .divider{position:absolute;left:455px;top:20px;width:1px;height:410px;background:#e3e3e3}
.info{position:absolute;left:484px;display:flex;gap:17px;font-size:14px;line-height:25px;color:#333}
.info .dot{width:30px;height:30px;border-radius:50%;background:var(--navy);flex:none;display:flex;align-items:center;justify-content:center;margin-top:-2px}

.footer-brand{left:157px;top:3453px;font-size:26px;color:#fff}
.footer-brand i{width:26px;height:26px;background:#fff !important}
.fsep{top:3440px;width:1px;height:42px;background:rgba(255,255,255,.5)}
.finfo{top:3455px;display:flex;gap:10px;align-items:center;color:#fff;font-size:13.5px;line-height:20px}
.fnav{left:240px;top:3544px;width:724px;height:1px;background:rgba(255,255,255,.5)}
.fnav-link{top:3561px;color:#fff;font-size:14px}
.copy{left:147px;top:3637px;color:#fff;font-size:13px}
.social{top:3628px;width:26px;height:27px;border:1px solid #fff;border-radius:3px}
</style>
</head>
<body>

<div class="abs topbar">
  <span style="left:140px">
    <svg width="13" height="13" viewBox="0 0 14 14"><circle cx="7" cy="7" r="6" fill="none" stroke="#fff" stroke-width="1.3"/><path d="M7 3.5V7h2.5" fill="none" stroke="#fff" stroke-width="1.3"/></svg>
    <b>Open hours:</b> Mo-Fr from 9.00-13.00 &amp; 14.00-18.00
  </span>
  <span style="left:548px">
    <svg width="13" height="13" viewBox="0 0 14 14"><path d="M3 2h2.5l1 3-1.5 1a7 7 0 0 0 3 3l1-1.5 3 1V11a1.5 1.5 0 0 1-1.5 1.5A9.5 9.5 0 0 1 1.5 3.5 1.5 1.5 0 0 1 3 2z" fill="none" stroke="#fff" stroke-width="1.2"/></svg>
    <b>Telephone:</b> (555) 014-2290
  </span>
  <span style="left:826px">
    <svg width="14" height="11" viewBox="0 0 14 11"><rect x=".6" y=".6" width="12.8" height="9.8" fill="none" stroke="#fff" stroke-width="1.2"/><path d="M1 1l6 5 6-5" fill="none" stroke="#fff" stroke-width="1.2"/></svg>
    <b>Email:</b> contact@corvantillc.com
  </span>
</div>

<nav class="abs nav">
  <div class="brand"><i></i>Corvanti, LLC</div>
  <a class="active" style="left:345px">HOME</a>
  <a style="left:507px">SERVICES</a>
  <a style="left:707px">ABOUT US</a>
  <a style="left:900px">CONTACT US</a>
</nav>

<section class="abs hero" role="img" aria-label="Photo of business professionals meeting around an office table">
  <div class="shade"></div>
</section>
<div class="abs hero-label">Medical Billing and Consulting</div>
<h1 class="abs heading hero-title">Clearing the Path to Your<br>Medical Billing Success</h1>
<p class="abs hero-text">Minimize cash flow interruptions caused when employed billers are on vacation or sick. Pay only for the service you need rather than an employee you might not need. Credentialing and Credentialing Maintenance.</p>
<div class="abs btn-discover">Discover more</div>

<section class="about">
  <svg class="abs about-img" width="505" height="505" viewBox="0 0 505 505" role="img" aria-label="Diamond collage of photos showing medical office staff at work">
    <polygon points="252,4 370,122 252,240 134,122" fill="#8e9499"/>
    <polygon points="128,128 246,246 128,364 10,246" fill="#6f7378"/>
    <polygon points="376,128 494,246 376,364 258,246" fill="#7d8a98"/>
    <polygon points="252,252 370,370 252,488 134,370" fill="#b9b2ad"/>
    <circle cx="252" cy="250" r="66" fill="#fff"/>
    <circle cx="252" cy="250" r="24" fill="var(--teal)"/>
  </svg>
  <div class="abs eyebrow">ABOUT CORVANTI</div>
  <h2 class="abs heading">Your Medical Billing Partner</h2>
  <div class="abs rule"></div>
  <h3 class="abs heading">Revenue Optimization.</h3>
  <p class="abs">We are a Northeast Arkansas medical billing and consulting company dedicated to providing efficient revenue cycle management and customer service with minimal cash flow interruption to our clients. We maintain the workflow of claim submissions to let providers focus on patient care.</p>
  <div class="abs feature" style="left:617px">
    <svg width="50" height="50" viewBox="0 0 50 50" fill="none" stroke="var(--ink)" stroke-width="1.6"><circle cx="25" cy="25" r="17"/><circle cx="25" cy="25" r="7"/><path d="M25 2v14M25 34v14M2 25h14M34 25h14"/></svg>
    <span>HIPAA<br>Complaint</span>
  </div>
  <div class="abs feature" style="left:910px">
    <svg width="38" height="38" viewBox="0 0 38 38" fill="none" stroke="var(--ink)" stroke-width="1.6"><path d="M19 3l15 11-6 19H10L4 14z"/></svg>
    <span>Results<br>Driven</span>
  </div>
  <div class="abs btn-contact">Contact us
    <svg width="18" height="12" viewBox="0 0 18 12" fill="none" stroke="#fff" stroke-width="1.6"><path d="M0 6h16M11 1l5 5-5 5"/></svg>
  </div>
</section>

<section class="abs services"></section>
<div class="abs center eyebrow" style="top:1540px">OUR SERVICES</div>
<h2 class="abs center heading" style="top:1565px;font-size:37px;font-weight:400">Services We Provide</h2>
<div class="abs rule" style="left:557px;top:1627px;width:86px"></div>
<p class="abs center" style="top:1656px;font-size:14.5px;line-height:24px;color:var(--grey-text);font-weight:300">Our mission is to streamline the complex process of medical billing and maintain the seamless<br>workflow of claim submissions.</p>

<div class="abs card-img" style="left:94px;background:linear-gradient(135deg,#c8cdd2,#8f9aa3)" role="img" aria-label="Photo of two doctors reviewing a tablet"></div>
<div class="abs card-img" style="left:440px;background:linear-gradient(135deg,#aab4c0,#e6e7e9)" role="img" aria-label="Photo of a doctor holding a tablet in a clinic"></div>
<div class="abs card-img" style="left:788px;background:linear-gradient(135deg,#3d4346,#7a7f80)" role="img" aria-label="Photo of two colleagues reviewing work on a laptop"></div>

<div class="abs card-tag" style="left:120px"><span class="ico"><svg width="30" height="30" viewBox="0 0 30 30" fill="none" stroke="#fff" stroke-width="1.4"><circle cx="15" cy="15" r="10"/><circle cx="15" cy="15" r="4"/><path d="M15 2v6M15 22v6M2 15h6M22 15h6"/></svg></span>Patient Billing</div>
<div class="abs card-tag" style="left:466px"><span class="ico"><svg width="30" height="30" viewBox="0 0 30 30" fill="none" stroke="#fff" stroke-width="1.4"><circle cx="15" cy="15" r="11"/><path d="M4 15h22M15 4a16 16 0 0 1 0 22M15 4a16 16 0 0 0 0 22"/><circle cx="21" cy="21" r="5" fill="var(--teal-bright)"/></svg></span>Provider Credentialing</div>
<div class="abs card-tag" style="left:813px"><span class="ico"><svg width="30" height="30" viewBox="0 0 30 30" fill="none" stroke="#fff" stroke-width="1.4"><circle cx="17" cy="9" r="5"/><path d="M6 24l8-8 3 3M4 27h22"/></svg></span>Workflow Analysis</div>

<section class="abs why" role="img" aria-label="Background photo of a medical team in discussion, tinted navy"></section>
<div class="abs center eyebrow" style="top:2178px;color:#fff">WHY CHOOSE CORVANTI</div>
<h2 class="abs center heading" style="top:2203px;font-size:37px;font-weight:400;color:#fff">Why Choose Us</h2>
<div class="abs rule" style="left:566px;top:2266px;width:86px"></div>

<div class="abs why-col" style="left:88px">
  <div class="circ"><svg width="34" height="30" viewBox="0 0 34 30" fill="none" stroke="var(--royal)" stroke-width="1.6"><circle cx="17" cy="9" r="5"/><circle cx="7" cy="11" r="3.5"/><circle cx="27" cy="11" r="3.5"/><path d="M8 27a9 9 0 0 1 18 0zM1 25a6 6 0 0 1 7-6M33 25a6 6 0 0 0-7-6"/></svg></div>
  <h4>Reduce Overhead</h4>
  <p>Pay only for the service you need rather<br>than an employee you might not need</p>
  <div class="appt">APPOINTMENT <svg width="22" height="10" viewBox="0 0 22 10" fill="none" stroke="#fff" stroke-width="1.4"><path d="M0 5h20M16 1l4 4-4 4"/></svg></div>
</div>
<div class="abs why-col" style="left:438px">
  <div class="circ"><svg width="34" height="30" viewBox="0 0 34 30" fill="none" stroke="var(--royal)" stroke-width="1.8"><path d="M5 26a14 14 0 1 1 24 0"/><path d="M17 20l-3-9"/><circle cx="17" cy="20" r="2"/></svg></div>
  <h4>Reduce Disruptions</h4>
  <p>Minimize cash flow interruptions caused when<br>employed billers are on vacation or sick</p>
  <div class="appt">APPOINTMENT <svg width="22" height="10" viewBox="0 0 22 10" fill="none" stroke="#fff" stroke-width="1.4"><path d="M0 5h20M16 1l4 4-4 4"/></svg></div>
</div>
<div class="abs why-col" style="left:782px">
  <div class="circ"><svg width="30" height="30" viewBox="0 0 30 30" fill="none" stroke="var(--royal)" stroke-width="1.8"><path d="M15 3l12 9-5 15H8L3 12z"/></svg></div>
  <h4>Reduce Headaches</h4>
  <p>We offer credentialing &nbsp;maintenance<br>to ensure your practice remains up-to-date</p>
  <div class="appt">APPOINTMENT <svg width="22" height="10" viewBox="0 0 22 10" fill="none" stroke="#fff" stroke-width="1.4"><path d="M0 5h20M16 1l4 4-4 4"/></svg></div>
</div>

<div class="abs center eyebrow" style="top:2725px">CONTACT US</div>
<h2 class="abs center heading" style="top:2751px;font-size:37px;font-weight:400">Get in touch with us</h2>
<div class="abs rule" style="left:564px;top:2813px;width:86px"></div>
<p class="abs center" style="top:2842px;font-size:14.5px;line-height:24px;color:var(--grey-text);font-weight:300">Feel free to contact us anytime to learn more about how we can assist your practice and<br>enhance your revenue management.</p>

<svg class="abs wave" width="1200" height="583" viewBox="0 0 1200 583">
  <path d="M0 70 Q120 160 260 210 Q600 290 900 200 Q1060 160 1200 190 L1200 583 L0 583 Z" fill="var(--navy)"/>
</svg>

<div class="abs card">
  <div class="topline"></div>
  <h3 class="heading">Feel free to write us<br>for billing services</h3>
  <div class="field" style="top:136px;height:42px">Full Name</div>
  <div class="field" style="top:188px;height:42px">Enter Email address</div>
  <div class="field" style="top:241px;height:73px">Your Messages</div>
  <div class="submit">SUBMIT NOW</div>
  <div class="divider"></div>
  <div class="info" style="top:59px"><span class="dot"><svg width="12" height="15" viewBox="0 0 12 15" fill="none" stroke="#fff" stroke-width="1.3"><path d="M6 14s5-5 5-8.5a5 5 0 0 0-10 0C1 9 6 14 6 14z"/><circle cx="6" cy="5.5" r="1.8"/></svg></span><span>Corvanti, LLC<br>18 Meadow Lane, Suite 4<br>Ashford, AR 72000<br>Northeast Arkansas, USA</span></div>
  <div class="info" style="top:173px"><span class="dot"><svg width="14" height="14" viewBox="0 0 14 14" fill="none" stroke="#fff" stroke-width="1.2"><path d="M3 2h2.5l1 3-1.5 1a7 7 0 0 0 3 3l1-1.5 3 1V11a1.5 1.5 0 0 1-1.5 1.5A9.5 9.5 0 0 1 1.5 3.5 1.5 1.5 0 0 1 3 2z"/></svg></span><span>(555) 014-2290</span></div>
  <div class="info" style="top:231px"><span class="dot"><svg width="14" height="11" viewBox="0 0 14 11" fill="none" stroke="#fff" stroke-width="1.2"><rect x=".6" y=".6" width="12.8" height="9.8"/><path d="M1 1l6 5 6-5"/></svg></span><span style="color:var(--ink)">contact@corvantillc.com</span></div>
  <div class="info" style="top:283px"><span class="dot"><svg width="12" height="10" viewBox="0 0 12 10" fill="#fff"><path d="M0 0l6 5-6 5zM6 0l6 5-6 5z"/></svg></span><span>8 am - 5pm &nbsp;Mon - Fri</span></div>
  <div class="info" style="top:348px;left:491px"><span>Reach us here:</span></div>
</div>

<div class="abs brand footer-brand"><i></i>Corvanti, LLC</div>
<div class="abs fsep" style="left:412px"></div>
<div class="abs finfo" style="left:432px"><svg width="28" height="28" viewBox="0 0 28 28" fill="none" stroke="#fff" stroke-width="1.3"><circle cx="14" cy="14" r="12"/><path d="M2 14h24M14 2a18 18 0 0 1 0 24M14 2a18 18 0 0 0 0 24"/></svg><span>18 Meadow Lane, Suite 4<br>Ashford, AR 72000, USA</span></div>
<div class="abs fsep" style="left:666px"></div>
<div class="abs finfo" style="left:689px"><svg width="26" height="30" viewBox="0 0 26 30" fill="none" stroke="#fff" stroke-width="1.3"><rect x="2" y="2" width="14" height="26" rx="2"/><path d="M20 10a6 6 0 0 1 0 10M23 7a10 10 0 0 1 0 16"/></svg><span>PHONE<br>(555) 014-2290</span></div>
<div class="abs fsep" style="left:846px"></div>
<div class="abs finfo" style="left:865px"><svg width="28" height="26" viewBox="0 0 28 26" fill="none" stroke="#fff" stroke-width="1.3"><path d="M2 10l12-8 12 8v14H2z"/><path d="M2 10l12 8 12-8"/></svg><span>EMAIL<br>contact@corvantillc.com</span></div>

<div class="abs fnav"></div>
<span class="abs fnav-link" style="left:277px">HOME</span>
<span class="abs fnav-link" style="left:390px">SERVICES</span>
<span class="abs fnav-link" style="left:528px">ABOUT US</span>
<span class="abs fnav-link" style="left:658px">TESTIMONIALS</span>
<span class="abs fnav-link" style="left:839px">CONTACT US</span>

<div class="abs copy">Corvanti Medical Billing</div>
<div class="abs social" style="left:933px"></div>
<div class="abs social" style="left:966px"></div>
<div class="abs social" style="left:999px"></div>
<div class="abs social" style="left:1032px"></div>

</body>
</html>
```